Header and footer for report

We would like a header and footer for our building management reports that incorporate a modern city skyline and our logo.

As well as update our other stationery.

```html
<!DOCTYPE html>
<html lang="en">
<head>
<meta charset="utf-8">
<title>Keel Partners — Letterhead</title>
<link href="https://fonts.googleapis.com/css2?family=Open+Sans:ital,wght@0,400;0,600;0,700;1,400&display=swap" rel="stylesheet">
<style>
  :root {
    --backdrop: #bcd8f1;
    --paper: #ffffff;
    --brand-blue: #1a62a8;
    --ink: #0c0c0c;
    --band-text: #ffffff;
  }
  * { box-sizing: border-box; margin: 0; padding: 0; }
  html, body {
    width: 1200px; height: 784px; overflow: hidden;
    background: var(--backdrop);
    font-family: "Open Sans", Arial, sans-serif;
  }
  .letterhead {
    position: absolute; left: 314px; top: 22px;
    width: 572px; height: 740px;
    background: var(--paper);
    box-shadow: 0 4px 14px rgba(40, 80, 130, 0.18);
  }
  .brand-square {
    position: absolute; left: 0; top: 26px;
    width: 44px; height: 30px;
    background: var(--brand-blue);
  }
  .brand-name {
    position: absolute; left: 56px; top: 34px;
    font-weight: 700; font-size: 22px; letter-spacing: 1px;
    color: var(--ink); text-transform: uppercase; line-height: 1;
  }
  .contact-band {
    position: absolute; right: 0; top: 98px;
    width: 330px; height: 34px;
    background: var(--ink); color: var(--band-text);
    font-size: 7.2px; font-style: italic; line-height: 1.55;
    padding: 5px 10px 0 14px;
  }
  .contact-line { display: flex; align-items: center; gap: 3px; white-space: nowrap; }
  .contact-icon { width: 7px; height: 7px; flex: none; }
  .contact-sep { width: 4px; }
  .footer-rule {
    position: absolute; left: 0; right: 0; bottom: 0;
    height: 7px; display: flex; gap: 6px;
  }
  .footer-rule .seg-blue { background: var(--brand-blue); }
  .footer-rule .seg-black { background: var(--ink); }
  .seg-first { width: 26%; }
  .seg-middle { width: 32%; }
  .seg-last { flex: 1; }
</style>
</head>
<body>
  <div class="letterhead">
    <header>
      <div class="brand-square"></div>
      <div class="brand-name">Keel Partners</div>
      <div class="contact-band">
        <div class="contact-line">
          <svg class="contact-icon" viewBox="0 0 10 10" aria-hidden="true"><circle cx="5" cy="5" r="4.5" fill="#fff"/><circle cx="5" cy="4.3" r="1.4" fill="#0c0c0c"/></svg>
          <span>0000 Harbor Way, Ste 210, Oregon, 97201, United States</span>
        </div>
        <div class="contact-line">
          <svg class="contact-icon" viewBox="0 0 10 10" aria-hidden="true"><circle cx="5" cy="5" r="4.5" fill="#fff"/><path d="M3.3 2.8 L4.3 3.8 L3.8 4.6 Q4.6 5.9 5.6 6.3 L6.3 5.7 L7.2 6.7 L6.4 7.4 Q3.4 6.6 2.6 3.5 Z" fill="#0c0c0c"/></svg>
          <span>(000) 000-0000</span><span class="contact-sep"></span>
          <svg class="contact-icon" viewBox="0 0 10 10" aria-hidden="true"><circle cx="5" cy="5" r="4.5" fill="#fff"/><rect x="3" y="3" width="4" height="4" fill="#0c0c0c"/></svg>
          <span>(000) 000-0000</span><span class="contact-sep"></span>
          <svg class="contact-icon" viewBox="0 0 10 10" aria-hidden="true"><circle cx="5" cy="5" r="4.5" fill="#fff"/><rect x="2.6" y="3.2" width="4.8" height="3.4" fill="none" stroke="#0c0c0c" stroke-width="0.8"/><path d="M2.6 3.2 L5 5.2 L7.4 3.2" fill="none" stroke="#0c0c0c" stroke-width="0.8"/></svg>
          <span>info@keelpartners.com</span><span class="contact-sep"></span>
          <svg class="contact-icon" viewBox="0 0 10 10" aria-hidden="true"><circle cx="5" cy="5" r="4.5" fill="#fff"/><circle cx="5" cy="5" r="2.4" fill="none" stroke="#0c0c0c" stroke-width="0.7"/><path d="M2.6 5 H7.4 M5 2.6 V7.4" stroke="#0c0c0c" stroke-width="0.6"/></svg>
          <span>www.keelpartners.com</span>
        </div>
      </div>
    </header>
    <footer class="footer-rule">
      <div class="seg-blue seg-first"></div>
      <div class="seg-black seg-middle"></div>
      <div class="seg-blue seg-last"></div>
    </footer>
  </div>
</body>
</html>
```